Business Card Design

Divorce
Collaborative Family Law
Family Dispute Resolution
Family Law Property & Children

Target Market(s)

Australia

Industry/Entity Type

Business

Contact Information for Business Card

Delphine Hartwell
M App Law (Family Law) LLB (Hons) BA (Hons) Ass Dip Ag (HH)
Family Dispute Resolution Provider
Hartwell Family Law
PO Box 4723 Fernleigh 3999
Phone 03 58217000 Fax 03 58217100 Email hartwellfamilylaw@quillnet.example

Colors
f04a51

Requirements
Should not have
• Any reference to
United States or US terminology
the word Company

```html
<!DOCTYPE html>
<html lang="en">
<head>
<meta charset="utf-8">
<title>Hartwell Family Law – Business Card</title>
<link rel="stylesheet" href="https://fonts.googleapis.com/css2?family=Marcellus+SC&display=swap">
<style>
  :root {
    --page-bg: #e9e6e1;
    --card-black: #0b0b0b;
    --card-charcoal: #1c1c1c;
    --accent-red: #f04a51;
    --card-font: "Marcellus SC", serif;
  }
  * { margin: 0; padding: 0; box-sizing: border-box; }
  html, body {
    width: 1200px;
    height: 900px;
    overflow: hidden;
    background: var(--page-bg);
  }
  .canvas {
    position: relative;
    width: 1200px;
    height: 900px;
  }
  .business-card {
    position: absolute;
    left: 120px;
    top: 157px;
    width: 960px;
    height: 586px;
    background: var(--card-black);
    overflow: hidden;
    font-family: var(--card-font);
    color: var(--accent-red);
    box-shadow: 0 14px 34px rgba(0, 0, 0, 0.28);
  }
  .card-texture {
    position: absolute;
    inset: 0;
    background: radial-gradient(ellipse at 45% 40%, var(--card-charcoal) 0%, var(--card-black) 75%);
  }
  .card-content {
    position: absolute;
    inset: 0;
  }
  .holder-name {
    position: absolute;
    left: 255px;
    top: 72px;
    font-size: 52px;
    font-weight: 400;
    letter-spacing: 3px;
    line-height: 1;
    white-space: nowrap;
    text-shadow: 0 2px 2px rgba(0, 0, 0, 0.8);
  }
  .rule {
    position: absolute;
    height: 5px;
    background: var(--accent-red);
  }
  .rule-top { left: 70px; right: 70px; top: 150px; }
  .rule-bottom { left: 70px; right: 70px; top: 318px; }
  .credentials {
    position: absolute;
    left: 70px;
    top: 172px;
    font-size: 30px;
    line-height: 42px;
    letter-spacing: 0.5px;
    white-space: nowrap;
  }
  .contact-details {
    position: absolute;
    left: 70px;
    top: 350px;
    font-size: 24px;
    line-height: 36px;
    letter-spacing: 0.5px;
    white-space: nowrap;
  }
</style>
</head>
<body>
  <main class="canvas">
    <article class="business-card">
      <div class="card-texture" role="img" aria-label="Fine dark dotted card texture"></div>
      <div class="card-content">
        <h1 class="holder-name">Delphine Hartwell</h1>
        <div class="rule rule-top"></div>
        <p class="credentials">
          M App Law (Family Law) LLB (Hons) BA (Hons)<br>
          Ass Dip Ag (HH) Family Dispute Resolution Provider<br>
          Hartwell Family Law
        </p>
        <div class="rule rule-bottom"></div>
        <p class="contact-details">
          PO Box 4723 Fernleigh 3999<br>
          Phone 03 58217000<br>
          Fax 03 58217100<br>
          Email hartwellfamilylaw@quillnet.example
        </p>
      </div>
    </article>
  </main>
</body>
</html>
```